Luxury Business Card Design for High-End Window Treatments

Gilded Vantages
Custom Plantation Shutters & Architectural Shading Systems

⸻

BACK

Daniel Forsythe
Owner

Custom Interior & Exterior Window Treatments

919-482-7034
gildedvantages.com

I have included a picture that I’m hoping we can use on the back, but I’m also wondering if you can get rid of the ladder? Should we get rid of shutters , shades and blinds underneath Gilded Vantages?

Target Market(s)

High-end residential homeowners, custom home builders, architects, interior designers, and luxury renovation clients seeking premium plantation shutters and motorized architectural shading systems.

Industry/Entity Type

Custom Window treatments

Contact Information for Business Card

Front Gilded Vantages Custom Plantation Shutters Motorized Architectural Shading Systems BACK Daniel Forsythe Owner 919-482-7034 GildedVantages.com Custom Interior & Exterior Window Treatments By Appointment

Requirements
Nice to have
• Not 100% sure on nice to halves or the color but you can definitely check out my website to get a better understanding of what I’m trying to do

```html
<!DOCTYPE html>
<html lang="en">
<head>
<meta charset="utf-8">
<title>Gilded Vantages — Business Card</title>
<link rel="stylesheet" href="https://fonts.googleapis.com/css2?family=Sora:wght@300;400;600;700&display=swap">
<style>
  :root {
    --backdrop: #e3e3e3;
    --ink-black: #050505;
    --gold: #d9b53a;
    --gold-deep: #6b5a16;
    --gold-panel: rgba(201, 170, 58, 0.92);
    --panel-dark: rgba(40, 40, 38, 0.85);
    --white: #ffffff;
    --text-dark: #111111;
  }
  * { box-sizing: border-box; margin: 0; padding: 0; }
  html, body {
    width: 804px; height: 1200px; overflow: hidden;
    background: var(--backdrop);
    font-family: "Sora", sans-serif;
  }
  .card {
    position: absolute; left: 82px; width: 640px; height: 366px; overflow: hidden;
    box-shadow: 0 18px 22px -14px rgba(0,0,0,0.45);
  }
  .card--front {
    top: 194px;
    background:
      radial-gradient(ellipse 260px 160px at 100% 0%, rgba(130,110,30,0.75), transparent 70%),
      radial-gradient(ellipse 300px 140px at 0% 100%, rgba(130,110,30,0.8), transparent 70%),
      var(--ink-black);
  }
  .front__headline-panel {
    position: absolute; left: 191px; top: 43px; width: 408px; height: 175px;
    background: var(--panel-dark); border-radius: 10px;
  }
  .front__photo {
    position: absolute; left: 39px; top: 31px; width: 198px; height: 302px;
    border: 1.5px solid var(--gold); border-radius: 8px;
    background: linear-gradient(160deg, #e9ddc7 0%, #b96a32 35%, #8a4a22 60%, #d8b68a 85%, #f0e2c8 100%);
  }
  .front__title {
    position: absolute; left: 264px; top: 76px;
    font-size: 29px; font-weight: 600; color: var(--gold); letter-spacing: -0.5px;
  }
  .front__subtitle {
    position: absolute; left: 264px; top: 111px;
    font-size: 19px; font-weight: 600; color: var(--white);
  }
  .front__service {
    position: absolute; left: 264px; top: 152px;
    font-size: 19px; font-weight: 300; color: var(--white); line-height: 1.2;
  }
  .front__brand {
    position: absolute; left: 264px; top: 270px; width: 130px;
    font-size: 20px; font-weight: 300; color: var(--gold); line-height: 1.15;
  }
  .front__contact { position: absolute; left: 436px; top: 264px; color: var(--white); }
  .front__name { font-size: 17px; font-weight: 400; color: var(--gold); }
  .front__role-line { margin-top: 10px; font-size: 15px; display: flex; align-items: baseline; gap: 10px; }
  .front__role { font-size: 18px; color: var(--gold); }
  .front__web { margin-top: 4px; font-size: 15px; display: flex; align-items: center; gap: 6px; }

  .card--back {
    top: 640px;
    background:
      linear-gradient(90deg, rgba(10,14,20,0.85) 0%, rgba(20,28,34,0.4) 45%, rgba(0,0,0,0) 80%),
      linear-gradient(180deg, #2c3d4a 0%, #4c5a5c 40%, #8c8a6c 70%, #3d4a30 100%);
  }
  .back__scene {
    position: absolute; inset: 0;
    background: linear-gradient(90deg, transparent 60%, rgba(196,160,96,0.6) 88%, rgba(210,170,100,0.75) 100%);
  }
  .back__panel {
    position: absolute; left: 40px; top: 39px; width: 307px; height: 289px;
    background: var(--gold-panel); border-radius: 8px;
  }
  .back__headline {
    position: absolute; left: 27px; top: 24px;
    font-size: 24px; font-weight: 600; color: var(--white); line-height: 1.15; letter-spacing: -0.4px;
  }
  .back__service {
    position: absolute; left: 27px; top: 88px;
    font-size: 20px; font-weight: 400; color: var(--text-dark); line-height: 1.25;
  }
  .back__name {
    position: absolute; left: 27px; top: 166px;
    font-size: 22px; font-weight: 400; color: var(--white);
  }
  .back__role {
    position: absolute; left: 27px; top: 193px;
    font-size: 15px; color: var(--white);
  }
  .back__line {
    position: absolute; left: 27px; display: flex; align-items: center; gap: 9px;
    font-size: 19px; font-weight: 300; color: var(--text-dark);
  }
  .back__line--phone { top: 217px; }
  .back__line--web { top: 244px; }
</style>
</head>
<body>

<section class="card card--front">
  <div class="front__headline-panel"></div>
  <div class="front__photo" role="img" aria-label="Interior room with tall wooden plantation shutters and sunlit floor"></div>
  <h1 class="front__title">GILDED VANTAGES</h1>
  <p class="front__subtitle">Custom Plantation Shutters</p>
  <p class="front__service">Motorizes Architectural<br>Shading Systems</p>
  <p class="front__brand">Gilded<br>Vantages</p>
  <div class="front__contact">
    <p class="front__name">Daniel Forsythe</p>
    <p class="front__role-line"><span class="front__role">Owner</span><span>919 482 7034</span></p>
    <p class="front__web">
      <svg width="10" height="12" viewBox="0 0 10 12"><path d="M0 0 L10 7 L5.5 7.5 L8 12 L6.5 12 L4 8 L0 11 Z" fill="#ffffff"/></svg>
      gildedvantages.com
    </p>
  </div>
</section>

<section class="card card--back">
  <div class="back__scene" role="img" aria-label="Evening view of a brick home porch with exterior motorized shades and landscaped garden"></div>
  <div class="back__panel">
    <h2 class="back__headline">CUSTOM INTERIOR<br>AND EXTERIOR</h2>
    <p class="back__service">Window Treatments<br>By Appointment</p>
    <p class="back__name">Daniel Forsythe</p>
    <p class="back__role">Owner</p>
    <p class="back__line back__line--phone">
      <svg width="14" height="14" viewBox="0 0 24 24"><path d="M6.6 10.8a15.1 15.1 0 0 0 6.6 6.6l2.2-2.2a1 1 0 0 1 1-.25 11.4 11.4 0 0 0 3.6.57 1 1 0 0 1 1 1V20a1 1 0 0 1-1 1A17 17 0 0 1 3 4a1 1 0 0 1 1-1h3.5a1 1 0 0 1 1 1c0 1.25.2 2.45.57 3.57a1 1 0 0 1-.25 1z" fill="#111111"/></svg>
      919-482-7034
    </p>
    <p class="back__line back__line--web">
      <svg width="12" height="14" viewBox="0 0 10 12"><path d="M0 0 L10 7 L5.5 7.5 L8 12 L6.5 12 L4 8 L0 11 Z" fill="#ffffff"/></svg>
      gildedvantages.com
    </p>
  </div>
</section>

</body>
</html>
```